Web Design Project for Qolvine Enterprises

Qolvine Enterprises is a small company with expertise in manufacturing, product development, global sourcing and retail. We provide sales/broker, import/export, private label and product development services to both manufacturers and retailers of food, beverage, health and beauty care and general merchandise. Would like a web site that incorporates images that inspire confidence in the areas of international trade and product development as well as convey the experience of founder and CEO in these areas.

Own web address qolvineenterprises.net and have hosting from brimport.com

Target Market(s)

Retail and manufacturing professionals.

Industry/Entity Type

It Company

Font styles to use
Serif
Sans Serif

Requirements
Must have
• Tabs for: Home, About Us, Services, Contact Us

```html
<!DOCTYPE html>
<html lang="en">
<head>
<meta charset="utf-8">
<title>Qolvine Enterprises</title>
<link href="https://fonts.googleapis.com/css2?family=Mulish:wght@400;600;700;800&family=Arimo:wght@400;700&display=swap" rel="stylesheet">
<style>
:root{
  --navy:#0a4fa0;
  --sky:#78b7e2;
  --ink:#3b4556;
  --text:#5d6677;
  --footer:#d0d0d0;
  --white:#ffffff;
  --slate:#5b6c86;
}
*{margin:0;padding:0;box-sizing:border-box}
html,body{width:1082px;height:1200px;overflow:hidden;background:var(--white)}
body{position:relative;font-family:"Arimo",Arial,sans-serif;color:var(--text)}
.abs{position:absolute}
.heading{font-family:"Mulish",Arial,sans-serif}

/* header */
.brand{left:99px;top:24px;display:flex;align-items:center;gap:8px}
.brand-dot{width:30px;height:30px;border-radius:50%;background:var(--navy)}
.brand-name{font-family:"Mulish",sans-serif;font-weight:800;font-size:19px;color:var(--navy)}
.main-nav{top:37px;right:112px;display:flex;gap:25px;font-family:"Mulish",sans-serif;font-weight:700;font-size:13px;color:var(--navy);text-transform:uppercase}
.main-nav .current{color:#2b2b2b}

/* hero */
.sky-band{left:0;top:108px;width:1082px;height:406px;background:var(--sky)}
.hero-frame{left:98px;top:85px;width:885px;height:399px;background:var(--white);box-shadow:0 8px 8px -4px rgba(0,0,0,.35)}
.hero-photo{left:107px;top:85px;width:867px;height:391px;background:linear-gradient(160deg,#eef3f5 0%,#c9d5dc 40%,#8d9aa3 70%,#4b5560 100%)}
.hero-caption{left:107px;top:414px;width:867px;height:62px;background:rgba(40,40,40,.78)}
.hero-title{left:141px;top:426px;font-family:"Mulish",sans-serif;font-weight:700;font-size:18px;color:var(--white)}
.hero-text{left:141px;top:451px;font-size:11.5px;color:var(--white)}
.hero-btn{left:827px;top:425px;width:116px;height:41px;background:var(--navy);color:var(--white);font-family:"Mulish",sans-serif;font-weight:800;font-size:12.5px;display:flex;align-items:center;justify-content:center}

/* services */
.service-band{left:0;top:514px;width:1082px;height:188px;background:var(--navy)}
.service{top:545px;width:250px;color:var(--white)}
.service svg{display:block;margin:0 auto}
.service h3{font-family:"Mulish",sans-serif;font-weight:700;font-size:14.5px;text-align:center;margin-top:13px}
.service p{font-size:11px;line-height:13px;margin-top:9px}

/* content */
.col{top:766px;width:270px}
.col h2{font-family:"Mulish",sans-serif;font-weight:700;font-size:22px;color:var(--ink);margin-bottom:10px}
.col p{font-size:12.8px;line-height:15.2px}
.col .gap{margin-top:15px}
.thumb{float:left;width:152px;height:104px;margin:-5px 10px 4px -2px;background:linear-gradient(180deg,#dfe3e6,#6c7480)}
.read-more{left:109px;top:952px;width:116px;height:41px;background:var(--navy);color:var(--white);font-size:12.5px;display:flex;align-items:center;justify-content:center}

/* footer */
.footer{left:0;top:1062px;width:1082px;height:138px;background:var(--footer)}
.foot-h{top:1087px;font-family:"Mulish",sans-serif;font-weight:600;font-size:17px;color:var(--ink)}
.foot-links{top:1116px;font-size:11px;line-height:16.2px;color:var(--ink)}
.email{left:394px;top:1118px;width:209px;height:29px;background:var(--white);font-size:12.5px;color:#333;padding:7px 10px}
.go{left:608px;top:1118px;width:37px;height:29px;background:var(--slate);color:var(--white);font-size:13px;display:flex;align-items:center;justify-content:center}
.social{left:780px;top:1092px;display:flex;gap:12px}
.social span{width:22px;height:22px;border-radius:50%;background:var(--slate)}
.copy{left:780px;top:1126px;font-size:11px;color:var(--ink)}
.call{left:780px;top:1143px;font-size:16.5px;color:var(--ink)}
</style>
</head>
<body>

<header>
  <div class="abs brand"><span class="brand-dot"></span><span class="brand-name">Qolvine Enterprises</span></div>
  <nav class="abs main-nav">
    <span class="current">Home</span><span>About Us</span><span>Services</span><span>Latest News</span><span>Contact Us</span>
  </nav>
</header>

<section>
  <div class="abs sky-band"></div>
  <div class="abs hero-frame"></div>
  <div class="abs hero-photo" role="img" aria-label="Business team meeting around an office table"></div>
  <div class="abs hero-caption"></div>
  <div class="abs hero-title">INVESTMENT PHILOSOPHY</div>
  <div class="abs hero-text">Duis aute irure dolor in reprehenderit in voluptate velit esse cillum dolore eu fugiat nulla pariatur.</div>
  <div class="abs hero-btn">LEARN MORE ›</div>
</section>

<section>
  <div class="abs service-band"></div>
  <div class="abs service" style="left:118px">
    <svg width="50" height="48" viewBox="0 0 50 48"><path d="M4 42 L18 28 L26 34 L42 14" fill="none" stroke="#fff" stroke-width="5"/><path d="M34 10 L46 8 L44 20 Z" fill="#fff"/></svg>
    <h3>PRODUCT DEVELOPMENT</h3>
    <p>Lorem ipsum dolor sit amet, consectetur adipisicing elit, sed do eiusmod tempor incididunt ut labore et dolore magna aliqua.</p>
  </div>
  <div class="abs service" style="left:414px">
    <svg width="50" height="48" viewBox="0 0 50 48"><rect x="6" y="10" width="12" height="36" rx="4" fill="#fff"/><circle cx="31" cy="32" r="13" fill="#fff"/><text x="31" y="38" font-size="16" font-weight="700" text-anchor="middle" fill="#0a4fa0" font-family="Arimo,sans-serif">$</text></svg>
    <h3>SALES/BROKER</h3>
    <p>Duis aute irure dolor in reprehenderit in voluptate velit esse cillum dolore eu fugiat nulla pariatur. Excepteur sint occaecat cupidatat non proident.</p>
  </div>
  <div class="abs service" style="left:708px">
    <svg width="50" height="48" viewBox="0 0 50 48"><rect x="4" y="18" width="9" height="20" rx="3" fill="#fff"/><rect x="20" y="6" width="10" height="32" rx="3" fill="#fff"/><rect x="37" y="18" width="9" height="20" rx="3" fill="#fff"/><ellipse cx="25" cy="42" rx="20" ry="4" fill="none" stroke="#fff" stroke-width="2"/></svg>
    <h3>IMPORT/EXPORT</h3>
    <p>Sed ut perspiciatis, unde omnis iste natus error sit voluptatem accusantium doloremque laudantium, totam rem aperiam eaque ipsa, quae ab illo.</p>
  </div>
</section>

<main>
  <article class="abs col" style="left:110px;width:260px">
    <h2>Who Choose Us</h2>
    <p>Lorem ipsum dolor sit amet, consectetur adipisicing elit, sed do eiusmod tempor incididunt ut labore et dolore magna aliqua.</p>
    <p class="gap">Ut enim ad minim veniam, quis nostrud exercitation ullamco laboris nisi ut aliquip ex ea commodo consequat. Duis aute irure dolor in reprehenderit in voluptate velit esse cillum dolore eu fugiat nulla pariatur.</p>
  </article>
  <div class="abs read-more">read more</div>

  <article class="abs col" style="left:401px;width:282px">
    <h2>Experiences</h2>
    <div class="thumb" role="img" aria-label="Three smiling business professionals standing together"></div>
    <p>Lorem ipsum dolor sit amet, consectetur adipisicing elit, sed do eiusmod tempor incididunt ut labore et dolore magna aliqua.</p>
    <p style="clear:both;width:262px">Ut enim ad minim veniam, quis nostrud exercitation ullamco laboris nisi ut aliquip ex ea commodo consequat. Duis aute irure dolor in reprehenderit in voluptate velit esse cillum dolore eu fugiat nulla pariatur.</p>
  </article>

  <article class="abs col" style="left:695px;width:282px">
    <h2>About Qolvine</h2>
    <div class="thumb" style="margin-left:1px" role="img" aria-label="Business team gathered around a laptop"></div>
    <p>Lorem ipsum dolor sit amet, consectetur adipisicing elit, sed do eiusmod tempor incididunt ut labore et dolore magna aliqua.</p>
    <p style="clear:both;width:262px">Ut enim ad minim veniam, quis nostrud exercitation ullamco laboris nisi ut aliquip ex ea commodo consequat. Duis aute irure dolor in reprehenderit in voluptate velit esse cillum dolore eu fugiat nulla pariatur.</p>
  </article>
</main>

<footer>
  <div class="abs footer"></div>
  <div class="abs foot-h" style="left:104px">Navigation</div>
  <div class="abs foot-links" style="left:105px">Home<br>Who we are<br>What we do</div>
  <div class="abs foot-links" style="left:203px">Who we serve<br>Education<br>Contact us</div>
  <div class="abs foot-h" style="left:395px">Newslitter Signup</div>
  <div class="abs email">enter email</div>
  <div class="abs go">go</div>
  <div class="abs social"><span></span><span></span><span></span><span></span></div>
  <div class="abs copy">Copyright © 2014 | Terms | Privacy</div>
  <div class="abs call">CALL US: 1 800 555 0184</div>
</footer>

</body>
</html>
```